Design our letter, business card, powerpoint and more

We have a logo and want a design for our business use. Letters (word template), business card (for printing) powerpoint presentation (template) and more.

```html
<!DOCTYPE html>
<html lang="en">
<head>
<meta charset="UTF-8">
<title>Our Company Service</title>
<link rel="stylesheet" href="https://fonts.googleapis.com/css2?family=Lato:wght@700&family=Open+Sans:wght@400&family=Oswald:wght@500&display=swap">
<style>
  :root {
    --brand-blue: #2f6aa6;
    --band-blue: rgba(78, 122, 202, 0.86);
    --accent-blue: #4472c4;
    --ink: #111111;
    --white: #ffffff;
    --photo-light: #d4d5d7;
    --photo-mid: #c4c6c9;
  }
  * { margin: 0; padding: 0; box-sizing: border-box; }
  html, body {
    width: 1200px;
    height: 675px;
    overflow: hidden;
    background: var(--white);
  }
  .slide {
    position: relative;
    width: 1200px;
    height: 675px;
    overflow: hidden;
    background: var(--white);
    color: var(--ink);
  }
  .title-block {
    position: absolute;
    left: 0; top: 0;
    width: 375px; height: 338px;
    background: var(--brand-blue);
    color: var(--white);
    font-family: "Lato", sans-serif;
    font-weight: 700;
  }
  .title-block .eyebrow {
    position: absolute;
    left: 43px; top: 139px;
    font-size: 22.5px;
  }
  .title-block .headline {
    position: absolute;
    left: 43px; top: 180px;
    font-size: 45px;
    line-height: 54px;
  }
  .details-rule {
    position: absolute;
    left: 47px; top: 406px;
    width: 78px; height: 4px;
    background: var(--accent-blue);
  }
  .details-title {
    position: absolute;
    left: 43px; top: 432px;
    font-family: "Lato", sans-serif;
    font-weight: 700;
    font-size: 22.5px;
  }
  .portrait {
    position: absolute;
    left: 375px; top: 0;
    width: 488px; height: 675px;
    background: linear-gradient(180deg, var(--photo-light) 0%, var(--photo-mid) 100%);
  }
  .summary-band {
    position: absolute;
    left: 0; top: 523px;
    width: 863px; height: 152px;
    background: var(--band-blue);
  }
  .summary-band p {
    position: absolute;
    left: 43px; top: 35px;
    width: 700px;
    font-family: "Open Sans", sans-serif;
    font-size: 20.5px;
    line-height: 27px;
    color: var(--white);
  }
  .service-list {
    position: absolute;
    left: 906px; top: 32px;
    width: 290px;
    list-style: none;
  }
  .service-item { height: 221px; }
  .service-number {
    font-family: "Oswald", sans-serif;
    font-weight: 500;
    font-size: 26px;
    line-height: 36px;
    color: var(--brand-blue);
  }
  .service-title {
    margin-top: 12px;
    font-family: "Lato", sans-serif;
    font-weight: 700;
    font-size: 22.5px;
    line-height: 30px;
  }
  .service-text {
    margin-top: 8px;
    font-family: "Open Sans", sans-serif;
    font-size: 20.5px;
    line-height: 27px;
    width: 244px;
  }
</style>
</head>
<body>
  <main class="slide">
    <section class="title-block">
      <p class="eyebrow">Our Service</p>
      <h1 class="headline">Our Company<br>Service</h1>
    </section>

    <div class="details-rule"></div>
    <h2 class="details-title">Company Service Details</h2>

    <div class="portrait" role="img" aria-label="Portrait photo of a smiling businessman in a navy blazer holding a coffee cup, on a light grey backdrop"></div>

    <section class="summary-band">
      <p>Pellentesque habitant morbi tristique senectus et netus et malesuada fames ac turpis egestas. Nunc ut elementum ligula. Quisque consequat justo ligula, vitae laoreet magna bibendum at.</p>
    </section>

    <ol class="service-list">
      <li class="service-item">
        <div class="service-number">01.</div>
        <h3 class="service-title">List down services</h3>
        <p class="service-text">Quisque consequat justo ligula, vitae laoreet magna</p>
      </li>
      <li class="service-item">
        <div class="service-number">02.</div>
        <h3 class="service-title">List down services</h3>
        <p class="service-text">Quisque consequat justo ligula, vitae laoreet magna</p>
      </li>
      <li class="service-item">
        <div class="service-number">03.</div>
        <h3 class="service-title">List down services</h3>
        <p class="service-text">Quisque consequat justo ligula, vitae laoreet magna</p>
      </li>
    </ol>
  </main>
</body>
</html>
```